Studying Effectively To Do List

I am looking to design a new "Study To Do List" for High School students (Ages 15 - 18) . This will be printed as an A4 notepad and so should only be a single A4 page.

The Design will need to be professional and look semi-serious but also be appealing to High school students (Ages 15 - 18) and should NOT be gender specific.

I have attached a word document outlining the structure of the page. The space provided should be large enough that people can write in it comfortably.

The notepad will most likely be printed in black and white but I'm also looking at coloured options - colours should be kept to a minimum.

This will be printed professionally and should also include a 3mm bleed.

The design should also include the business logo (included in the word document)

Target Market(s)

High School students (Ages 15 - 18). Both genders

Industry/Entity Type

Education

Font styles to use
Serif
Sans Serif

Requirements
Must have
• Please see the word document attached.
Should not have
• Too much colour

```html
<!DOCTYPE html>
<html lang="en">
<head>
<meta charset="utf-8">
<title>Study To Do List</title>
<link rel="stylesheet" href="https://fonts.googleapis.com/css2?family=Jost:wght@300;400;500;600&display=swap">
<style>
  :root {
    --navy: #22304a;
    --slate: #5d5e60;
    --orange: #f08a35;
    --line: #f2a868;
    --field-grey: #e6e7e9;
    --field-cream: #fff8d6;
    --paper: #ffffff;
    --backdrop: #ededed;
  }
  * { box-sizing: border-box; margin: 0; padding: 0; }
  html, body { width: 1200px; height: 1192px; overflow: hidden; background: var(--backdrop); font-family: "Jost", sans-serif; }
  .sheet {
    position: absolute; left: 179px; top: 0;
    width: 818px; height: 1157px;
    background: var(--paper);
    transform: scale(1.0303); transform-origin: top left;
  }
  .abs { position: absolute; }

  .date-field { left: 38px; top: 89px; width: 171px; height: 28px; border: 1px solid var(--slate); }
  .date-label {
    position: absolute; left: 0; top: 0; height: 100%; width: 62px;
    background: var(--navy); color: #fff; font-weight: 600; font-size: 14px;
    line-height: 26px; padding-left: 7px;
    clip-path: polygon(0 0, 100% 0, 82% 100%, 0 100%);
  }

  .brand { left: 640px; top: 60px; display: flex; align-items: center; gap: 10px; }
  .brand-dot { width: 22px; height: 22px; border-radius: 50%; background: var(--orange); }
  .brand-name { font-size: 44px; font-weight: 600; color: var(--navy); letter-spacing: 1px; }

  .section-title { left: 36px; font-weight: 300; font-size: 40px; letter-spacing: 2px; line-height: 1; color: var(--navy); }
  .section-title.accent { color: var(--orange); }

  .num-grid { border: 1px solid var(--line); }
  .num-row { position: absolute; height: 21px; border-bottom: 1px solid var(--line); }
  .num-row:last-child { border-bottom: none; }
  .num {
    position: absolute; top: 0; width: 20px; height: 21px;
    color: #fff; font-weight: 500; font-size: 15px; line-height: 21px; text-align: center;
  }
  .num.dark { background: var(--navy); }
  .num.mid { background: var(--slate); }

  .field-row { position: absolute; left: 38px; width: 741px; height: 24px; }
  .field-row.grey { background: var(--field-grey); }
  .field-row.cream { background: var(--field-cream); }
  .field-label {
    position: absolute; left: 0; top: 0; height: 100%;
    color: #fff; font-weight: 600; font-size: 15px; line-height: 24px; padding-left: 9px;
  }
  .field-label.dark { background: var(--navy); }
  .field-label.mid { background: var(--slate); }
  .hw-label { width: 91px; }
  .as-label { width: 115px; font-size: 14.5px; letter-spacing: -0.3px; }
  .due-tag {
    position: absolute; left: 401px; top: 1px; width: 53px; height: 22px;
    background: var(--slate); color: #fff; font-weight: 600; font-size: 15px; line-height: 22px; text-align: center; letter-spacing: 1px;
  }

  .bottom-table { left: 38px; top: 1014px; width: 741px; height: 108px; border: 1px solid var(--line); }
  .col-head {
    position: absolute; top: 0; height: 23px; color: #fff; font-weight: 600; font-size: 15px;
    line-height: 23px; text-align: center;
  }
  .col-head.notes { left: 0; width: 396px; background: var(--orange); }
  .col-head.practice { left: 397px; width: 343px; background: var(--navy); }
  .col-divider { position: absolute; left: 396px; top: 23px; bottom: 0; width: 1px; background: var(--line); }

  .footer-band { left: 0; top: 1142px; width: 818px; height: 15px; }
</style>
</head>
<body>
<main class="sheet">
  <div class="abs date-field"><span class="date-label">Date:</span></div>

  <div class="abs brand"><span class="brand-dot"></span><span class="brand-name">KLA</span></div>

  <h2 class="abs section-title" style="top:155px">REVISION</h2>
  <section class="abs num-grid" style="left:38px; top:189px; width:741px; height:86px">
    <div class="num-row" style="top:0; width:100%"><span class="num dark" style="left:0">1</span><span class="num dark" style="left:370px">5</span></div>
    <div class="num-row" style="top:21px; width:100%"><span class="num mid" style="left:0">2</span><span class="num mid" style="left:370px">6</span></div>
    <div class="num-row" style="top:42px; width:100%"><span class="num dark" style="left:0">3</span><span class="num dark" style="left:370px">7</span></div>
    <div class="num-row" style="top:63px; width:100%"><span class="num mid" style="left:0">4</span><span class="num mid" style="left:370px">8</span></div>
  </section>

  <h2 class="abs section-title accent" style="top:300px">HOMEWORK</h2>
  <section class="homework">
    <div class="field-row grey" style="top:337px"><span class="field-label dark hw-label">SUBJECT:</span></div>
    <div class="field-row cream" style="top:361px"><span class="field-label mid hw-label">TASK:</span></div>
    <div class="field-row grey" style="top:391px"><span class="field-label dark hw-label">SUBJECT:</span></div>
    <div class="field-row cream" style="top:415px"><span class="field-label mid hw-label">TASK:</span></div>
    <div class="field-row grey" style="top:445px"><span class="field-label dark hw-label">SUBJECT:</span></div>
    <div class="field-row cream" style="top:469px"><span class="field-label mid hw-label">TASK:</span></div>
    <div class="field-row grey" style="top:500px"><span class="field-label dark hw-label">SUBJECT:</span></div>
    <div class="field-row cream" style="top:524px"><span class="field-label mid hw-label">TASK:</span></div>
    <div class="field-row grey" style="top:554px"><span class="field-label dark hw-label">SUBJECT:</span></div>
    <div class="field-row cream" style="top:578px"><span class="field-label mid hw-label">TASK:</span></div>
    <div class="field-row grey" style="top:608px"><span class="field-label dark hw-label">SUBJECT:</span></div>
    <div class="field-row cream" style="top:632px"><span class="field-label mid hw-label">TASK:</span></div>
  </section>

  <h2 class="abs section-title" style="top:682px">ASSESSMENTS</h2>
  <section class="assessments">
    <div class="field-row cream" style="top:717px"><span class="field-label mid as-label">ASSESSMENT:</span><span class="due-tag">DUE</span></div>
    <div class="field-row grey" style="top:741px"><span class="field-label dark as-label">ELEMENT:</span></div>
    <div class="field-row cream" style="top:772px"><span class="field-label mid as-label">ASSESSMENT:</span><span class="due-tag">DUE</span></div>
    <div class="field-row grey" style="top:796px"><span class="field-label dark as-label">ELEMENT:</span></div>
    <div class="field-row cream" style="top:827px"><span class="field-label mid as-label">ASSESSMENT:</span><span class="due-tag">DUE</span></div>
    <div class="field-row grey" style="top:851px"><span class="field-label dark as-label">ELEMENT:</span></div>
    <div class="field-row cream" style="top:883px"><span class="field-label mid as-label">ASSESSMENT:</span><span class="due-tag">DUE</span></div>
    <div class="field-row grey" style="top:907px"><span class="field-label dark as-label">ELEMENT:</span></div>
    <div class="field-row cream" style="top:938px"><span class="field-label mid as-label">ASSESSMENT:</span><span class="due-tag">DUE</span></div>
    <div class="field-row grey" style="top:962px"><span class="field-label dark as-label">ELEMENT:</span></div>
  </section>

  <section class="abs bottom-table">
    <div class="col-head notes">NOTES</div>
    <div class="col-head practice">PRACTICE</div>
    <div class="num-row" style="top:23px; width:100%"><span class="num dark" style="left:0">1</span><span class="num dark" style="left:198px">5</span></div>
    <div class="num-row" style="top:44px; width:100%"><span class="num mid" style="left:0">2</span><span class="num mid" style="left:198px">6</span></div>
    <div class="num-row" style="top:65px; width:100%"><span class="num dark" style="left:0">3</span><span class="num dark" style="left:198px">7</span></div>
    <div class="num-row" style="top:86px; width:100%; border-bottom:none"><span class="num mid" style="left:0">4</span><span class="num mid" style="left:198px">8</span></div>
    <div class="col-divider"></div>
  </section>

  <svg class="abs footer-band" viewBox="0 0 818 15" preserveAspectRatio="none" aria-hidden="true">
    <polygon points="0,0 375,0 405,15 0,15" fill="var(--navy)"/>
    <polygon points="392,0 818,0 818,15 420,15" fill="var(--orange)"/>
  </svg>
</main>
</body>
</html>
```